Patient Fact sheets for medical conditions and treatments

Hi,

I need a new design for my patient fact sheets. I am moving from my current clinic and I am looking from a new look.

I have attached
1. a current Fact sheet
2. New home page to the website
3. New Logo.

They need to be single page and easily readable for patients.

The will be in both PDF and print form in the future.

Target Market(s)

Patients with chronic pain age 40+

Font styles to use
Serif

Requirements
Must have
• My logo, should be inline with design elements on the Front page provided.

Please use the same font as the Logo

```html
<!DOCTYPE html>
<html lang="en">
<head>
<meta charset="utf-8">
<title>Fact Sheets – PRP</title>
<link href="https://fonts.googleapis.com/css2?family=Bebas+Neue&family=Open+Sans:wght@400;600;700&display=swap" rel="stylesheet">
<style>
  :root{
    --page-bg:#3a3a3a;
    --paper:#ffffff;
    --ink:#231a3d;
    --purple-dark:#24154a;
    --purple-mid:#3a2170;
    --blue:#4a7cc4;
    --rule:#c9c6d3;
    --body:#2b2b33;
  }
  *{box-sizing:border-box;margin:0;padding:0}
  html,body{width:1200px;height:1000px;overflow:hidden;background:var(--page-bg)}
  .sheet{position:absolute;left:288px;top:57px;width:624px;height:882px;background:var(--paper);overflow:hidden;font-family:"Open Sans",Arial,sans-serif;color:var(--body)}
  .shapes,.photo{position:absolute;left:0;top:0}
  .brand{position:absolute;left:34px;top:46px;font-family:"Open Sans",Arial,sans-serif;font-weight:600;color:var(--ink);font-size:30px;line-height:1.1;letter-spacing:.5px}
  .banner-title{position:absolute;left:32px;top:130px;font-family:"Bebas Neue",Impact,sans-serif;color:#fff;font-size:56px;letter-spacing:1px;line-height:1}
  .col-left{position:absolute;left:34px;top:208px;width:257px}
  .col-right{position:absolute;left:336px;top:218px;width:247px}
  h2{font-weight:700;font-size:17.5px;line-height:1.15;letter-spacing:.2px}
  .col-left h2{color:#fff}
  .rule{position:relative;height:1px;margin:9px 0 13px;background:var(--line)}
  .rule::before{content:"";position:absolute;left:0;top:-1px;width:38%;height:3px;background:var(--accent)}
  .on-dark{--accent:#fff;--line:#fff}
  .on-light{--accent:var(--purple-dark);--line:var(--rule)}
  p{font-size:8.4px;line-height:12.1px;text-align:justify;margin-bottom:4px}
  .col-left p{color:#ddd8ea}
  .section-gap{margin-top:13px}
  .role{position:absolute;left:34px;top:690px;width:250px}
  .role h2{color:var(--purple-dark)}
  .role p{font-weight:700;color:var(--ink)}
  .ticks{list-style:none}
  .ticks li{position:relative;padding-left:30px;font-size:8.4px;line-height:12.1px;margin-bottom:4px}
  .ticks li::before{content:"";position:absolute;left:0;top:1px;width:9px;height:9px;border-radius:50%;background:var(--purple-dark)}
  .ticks li::after{content:"";position:absolute;left:2.6px;top:3.2px;width:3px;height:1.6px;border-left:1.4px solid #fff;border-bottom:1.4px solid #fff;transform:rotate(-45deg)}
  .col-right h2{color:var(--purple-dark)}
  .treat{margin-top:36px}
  .subhead{font-weight:700;font-size:11px;color:var(--ink);margin:12px 0 18px}
  .uses{display:grid;grid-template-columns:159px 1fr;row-gap:9px}
  .use{display:flex;align-items:center;gap:8px;font-weight:700;font-size:10.2px;line-height:1.15;color:var(--ink);height:28px}
  .use svg{flex:none}
  .results{margin-top:36px;margin-left:10px}
  .divider{position:absolute;left:311px;top:198px;width:1.5px;height:592px;background:#bdbdc6}
  .contact{position:absolute;left:34px;top:810px;color:#fff;font-weight:600;font-size:10.6px}
  .contact li{list-style:none;display:flex;gap:10px;align-items:flex-start;margin-bottom:5px;line-height:1.4}
  .contact svg{margin-top:2px}
  .phones{position:absolute;left:304px;top:834px;display:flex;align-items:center;gap:14px;font-family:"Bebas Neue",Impact,sans-serif;color:#fff;font-size:25px;letter-spacing:.3px}
  .phones span{display:flex;align-items:center;gap:8px}
  .phones .sep{width:1px;height:32px;background:#8f83b8}
</style>
</head>
<body>
<main class="sheet">
  <svg class="shapes" width="624" height="882" viewBox="0 0 624 882" aria-hidden="true">
    <defs>
      <linearGradient id="band" x1="0" x2="1">
        <stop offset="0" stop-color="#2b1857"/><stop offset="1" stop-color="#5a36a0"/>
      </linearGradient>
      <linearGradient id="photoTone" x1="0" y1="0" x2="1" y2="1">
        <stop offset="0" stop-color="#f1f1f1"/><stop offset=".55" stop-color="#b9b9b9"/><stop offset="1" stop-color="#e6e6e6"/>
      </linearGradient>
    </defs>
    <polygon points="0,115 322,115 282,198 0,198" fill="url(#band)"/>
    <polygon points="366,0 378,0 281,198 269,198" fill="var(--blue)"/>
    <rect x="0" y="198" width="311" height="487" fill="var(--purple-dark)"/>
    <polygon points="0,800 318,800 290,882 0,882" fill="url(#band)"/>
    <polygon points="310,820 624,820 624,882 282,882" fill="var(--purple-mid)"/>
  </svg>

  <svg class="photo" width="624" height="198" viewBox="0 0 624 198" role="img" aria-label="Black and white photo of a gloved hand pipetting blood samples into test tubes in a rack">
    <polygon points="378,0 624,0 624,198 281,198" fill="url(#photoTone)"/>
  </svg>

  <div class="brand">Dr Sam Rowe</div>

  <div class="banner-title">FACT SHEETS</div>

  <section class="col-left">
    <h2>WHAT IS PRP?</h2>
    <div class="rule on-dark"></div>
    <p>Platelet-Rich Plasma (PRP) is concentrated platelets and white blood cells derived from your own blood.</p>
    <p>Platelet Rich Plasma Injection Therapy (PRP therapy), is a growing treatment approach for soft tissue injuries including tendon, muscle and ligaments. It is also showing good results for mild to moderate osteoarthritis.</p>
    <p>While this approach has been used overseas for many years, it's fairly new to Australia in the treatment of musculoskeletal and orthopaedic conditions.</p>

    <h2 class="section-gap">HOW DOES PRP WORK?</h2>
    <div class="rule on-dark"></div>
    <p>Some tissues in the body have a poor blood supply or respond poorly to excessive load, ultimately failing to heal naturally. While some of our primary treatment such as physiotherapy, massage, biomechanical correction and other forms of treatment are used to treat these soft tissue injuries, sometimes the body fails to respond.</p>
    <p>PRP therapy utilises the healing properties in blood to allow a healing reaction to occur in a tissue that's not healing on its own. Our blood has small granules called 'platelets', which contain special growth factors that when released, allow stem cells in the particular tissue to 'switch' on and cause new tissue to be created and heal the injured area.</p>
    <p>Take the example of achilles tendinopathy. If the achilles is painful, thickened and not responding to rehabilitation, then the sports physician will inject the PRP into the achilles which will cause the tendon cells (tenocytes/fibroblasts) to create new achilles collagen to strengthen the achilles. White blood cells also enter the area to mop up any achilles tissue that may have been damaged due to the ongoing pain and thickening in the area.</p>
  </section>

  <section class="role">
    <h2>ROLE OF PLATELETS &amp;<br>GROWTH FACTORS</h2>
    <div class="rule on-light"></div>
    <p>PRP contains highly concentrated platelets. Platelets have been identified to secrete growth factors, which are known to play a role in:</p>
  </section>

  <div class="divider"></div>

  <section class="col-right">
    <ul class="ticks">
      <li>Increasing tissue vascularity and increasing the rate of epithelial tissue production (wound healing)</li>
      <li>Attracting other cells that fight infection</li>
      <li>Acting as a seal during closures</li>
      <li>Providing an immediate surgical hemostatic agent (reduction of bleeding)</li>
      <li>Osteogenesis (bone regeneration and repair)</li>
    </ul>

    <div class="treat">
      <h2>WHAT CAN PRP TREAT?</h2>
      <div class="rule on-light"></div>
      <div class="subhead">PRP THERAPY CAN BE USED FOR:</div>
      <div class="uses">
        <div class="use"><svg width="28" height="28" viewBox="0 0 28 28"><circle cx="14" cy="14" r="14" fill="var(--purple-dark)"/><rect x="12" y="7" width="4" height="14" rx="2" fill="#fff"/></svg>Orthopedic<br>surgery</div>
        <div class="use"><svg width="28" height="28" viewBox="0 0 28 28"><circle cx="14" cy="14" r="14" fill="var(--purple-dark)"/><path d="M14 20l-5-5a3 3 0 015-4 3 3 0 015 4z" fill="#fff"/></svg>Cardiac<br>surgery</div>
        <div class="use"><svg width="28" height="28" viewBox="0 0 28 28"><circle cx="14" cy="14" r="14" fill="var(--purple-dark)"/><path d="M8 19l10-10 2 2-10 10z" fill="#fff"/></svg>Plastic and<br>cosmetic surgery</div>
        <div class="use"><svg width="28" height="28" viewBox="0 0 28 28"><circle cx="14" cy="14" r="14" fill="var(--purple-dark)"/><rect x="10" y="8" width="8" height="12" rx="3" fill="#fff"/></svg>Burn care</div>
        <div class="use"><svg width="28" height="28" viewBox="0 0 28 28"><circle cx="14" cy="14" r="14" fill="var(--purple-dark)"/><path d="M9 10h10v4l-2 6h-6l-2-6z" fill="#fff"/></svg>Oral maxillofacial<br>surgery</div>
        <div class="use"><svg width="28" height="28" viewBox="0 0 28 28"><circle cx="14" cy="14" r="14" fill="var(--purple-dark)"/><circle cx="14" cy="11" r="3.5" fill="#fff"/><rect x="9" y="16" width="10" height="5" rx="2" fill="#fff"/></svg>Neurosu-<br>rgery</div>
        <div class="use"><svg width="28" height="28" viewBox="0 0 28 28"><circle cx="14" cy="14" r="14" fill="var(--purple-dark)"/><path d="M11 8a5 6 0 016 5c0 4-3 6-5 6" stroke="#fff" stroke-width="2.2" fill="none"/></svg>Ear, nose,<br>surgery</div>
        <div class="use"><svg width="28" height="28" viewBox="0 0 28 28"><circle cx="14" cy="14" r="14" fill="var(--purple-dark)"/><rect x="8" y="12" width="12" height="4" rx="2" fill="#fff" transform="rotate(45 14 14)"/><rect x="8" y="12" width="12" height="4" rx="2" fill="#fff" transform="rotate(-45 14 14)"/></svg>Wound<br>healing</div>
        <div class="use"><svg width="28" height="28" viewBox="0 0 28 28"><circle cx="14" cy="14" r="14" fill="var(--purple-dark)"/><ellipse cx="14" cy="15" rx="6" ry="4" fill="#fff"/></svg>Throat (ENT)<br>surgery</div>
        <div class="use"><svg width="28" height="28" viewBox="0 0 28 28"><circle cx="14" cy="14" r="14" fill="var(--purple-dark)"/><path d="M9 20l10-12M13 19l6-7" stroke="#fff" stroke-width="2" fill="none"/></svg>Vascular<br>surgery</div>
      </div>
    </div>

    <div class="results">
      <h2>WHAT ARE THE EXPECTED<br>RESULTS OF PRP?</h2>
      <div class="rule on-light"></div>
      <p>Because the goal of PRP therapy is to resolve pain through healing, it could prove to have lasting results. Initial improvement may be seen within a few weeks, gradually increasing as the healing progresses. Research studies and clinical practice have shown PRP therapy to be very effective at relieving pain and returning patients to their normal lives. The need for surgery can also be greatly reduced by treating injured tissues before the damage progresses and the condition is irreversible.</p>
    </div>
  </section>

  <ul class="contact">
    <li><svg width="12" height="13" viewBox="0 0 12 13"><rect width="12" height="13" rx="2" fill="var(--blue)"/><path d="M6 10.5L3.6 6.6a2.6 2.6 0 114.8 0z" fill="#fff"/><circle cx="6" cy="5.3" r="1" fill="var(--blue)"/></svg><span>Northgate Pain Group Elm House, Ground<br>Floor 48 Harbour Road Westvale VIC 3999</span></li>
    <li><svg width="12" height="13" viewBox="0 0 12 13"><rect width="12" height="13" rx="2" fill="var(--blue)"/><rect x="2.5" y="4" width="7" height="5" fill="#fff"/><path d="M2.5 4l3.5 3 3.5-3" stroke="var(--blue)" stroke-width=".9" fill="none"/></svg><span>hello@northgatepain.example</span></li>
    <li><svg width="12" height="13" viewBox="0 0 12 13"><rect width="12" height="13" rx="2" fill="var(--blue)"/><circle cx="6" cy="6.5" r="3.3" stroke="#fff" stroke-width="1" fill="none"/><path d="M2.7 6.5h6.6M6 3.2v6.6" stroke="#fff" stroke-width=".8"/></svg><span>www.northgatepain.example</span></li>
  </ul>

  <div class="phones">
    <span><svg width="16" height="16" viewBox="0 0 16 16"><path d="M3 1.5l3 .5 1 3-2 1.5a9 9 0 004.5 4.5L11 9l3 1 .5 3-2 1.5C7 14 2 9 1.5 3.5z" fill="var(--blue)"/></svg>03 9000 1234</span>
    <i class="sep"></i>
    <span><svg width="20" height="16" viewBox="0 0 20 16"><rect x="5" y="1" width="10" height="5" fill="var(--blue)"/><rect x="1" y="6" width="18" height="7" rx="1.5" fill="var(--blue)"/><rect x="5" y="10" width="10" height="5" fill="#cfd9f0"/></svg>03 9000 1235</span>
  </div>
</main>
</body>
</html>
```